Brand new letterhead, business card, email signature etc.

We are a financial company in London, UK. Our website is www.quorvane.com. We're wanting a complete remodel of the company colours, letter head, business cards, email signatures, etc. Looking to keep the same font for the company name. I have upload a colour palette that we want to work with. We're looking for company letterhead for outgoing letters/ correspondence, letterhead for internal documentation, email signatures, e-letters. etc. Ultimately we will redesign the entire website also. It is important that our clients get a strong, secure, warm, trustworthy, solid feeling and first impression.
Updates

Designs look the same

Target Market(s)

Institutional investors, (ultra) high net worth individuals

Industry/Entity Type

Finance, Invesments banking.

Font styles to use
Other font styles liked:
• Current font is "Champagne & Limousines"

Requirements
Must have
• Must use the colours provided on the PDF uploaded to the portal. The purple = main colour. The red = accent colour.
Nice to have
• Nice to use same font as now for the company name "Marlowin". Font is "Champagne & Limousines". Nice to have some reference to the old logo flower, but only subtle.
Should not have
• Do not use the colour red from our website. Use the colours provided on the colour palette PDF that I uploaded in the portal.

```html
<!DOCTYPE html>
<html lang="en">
<head>
<meta charset="utf-8">
<title>Marlowin — Business Card</title>
<link rel="stylesheet" href="https://fonts.googleapis.com/css2?family=Josefin+Sans:wght@300&family=Montserrat:wght@700&family=Didact+Gothic&display=swap">
<style>
  :root {
    --backdrop: #232323;
    --main: #241a2b;
    --main-deep: #1d1523;
    --ink: #ffffff;
    --accent: #e03a26;
    --edge: #d8321f;
  }
  * { box-sizing: border-box; margin: 0; padding: 0; }
  html, body { width: 1200px; height: 780px; overflow: hidden; background: var(--backdrop); }
  .canvas { position: relative; width: 1200px; height: 780px; }

  .card {
    position: absolute; left: 320px; width: 560px; height: 320px;
    background: linear-gradient(160deg, var(--main) 0%, var(--main-deep) 100%);
    border-bottom: 6px solid var(--edge);
    box-shadow: 0 14px 30px rgba(0,0,0,.55);
    overflow: hidden;
  }
  .card--front { top: 45px; }
  .card--back { top: 415px; }

  /* front */
  .lockup {
    position: absolute; left: 0; right: 0; top: 50%;
    transform: translateY(-50%);
    display: flex; align-items: center; justify-content: center; gap: 26px;
  }
  .lockup__square { width: 62px; height: 62px; border: 1.5px solid var(--ink); flex: none; }
  .wordmark {
    font-family: "Josefin Sans", sans-serif; font-weight: 300;
    color: var(--ink); letter-spacing: .22em; text-transform: uppercase;
    white-space: nowrap;
  }
  .lockup .wordmark { font-size: 52px; line-height: 1; padding-top: 8px; }

  /* back */
  .side-mark {
    position: absolute; left: 24px; bottom: 24px;
    display: flex; flex-direction: column; align-items: flex-start; gap: 14px;
  }
  .side-mark .wordmark {
    writing-mode: vertical-rl; transform: rotate(180deg);
    font-size: 28px; line-height: 1; padding-left: 12px;
  }
  .side-mark__square { width: 52px; height: 52px; border: 1.5px solid var(--ink); }

  .accent-bar {
    position: absolute; right: 0; top: 52px; width: 26px; height: 52px;
    background: var(--accent);
  }
  .contact {
    position: absolute; right: 40px; top: 60px; text-align: right;
    font-family: "Didact Gothic", sans-serif; color: var(--ink);
  }
  .contact__name {
    font-family: "Montserrat", sans-serif; font-weight: 700;
    font-size: 30px; line-height: 1.05; letter-spacing: .01em;
  }
  .contact__first { color: var(--accent); }
  .contact__role { font-size: 15px; margin-top: 2px; }
  .contact__address { font-size: 15px; line-height: 1.3; margin-top: 16px; }
  .contact__lines { list-style: none; margin-top: 14px; font-size: 15px; line-height: 1.4; }
  .contact__lines li { display: flex; align-items: center; justify-content: flex-end; gap: 8px; }
  .contact__lines svg { width: 13px; height: 13px; flex: none; }
</style>
</head>
<body>
<main class="canvas">

  <section class="card card--front" aria-label="Business card front">
    <div class="lockup">
      <span class="lockup__square"></span>
      <span class="wordmark">Marlowin</span>
    </div>
  </section>

  <section class="card card--back" aria-label="Business card back">
    <div class="side-mark">
      <span class="wordmark">Marlowin</span>
      <span class="side-mark__square"></span>
    </div>

    <span class="accent-bar"></span>

    <div class="contact">
      <p class="contact__name"><span class="contact__first">Lenka</span> Varosova</p>
      <p class="contact__role">Managing Director</p>
      <p class="contact__address">1840 Aldermoor Rd. Suite 310<br>Harrow Vale, TX 76455</p>
      <ul class="contact__lines">
        <li>(555) 214-0387
          <svg viewBox="0 0 16 16" aria-hidden="true"><path fill="#e03a26" d="M4 1.5 6.2 4 5 5.6a8 8 0 0 0 5.4 5.4L12 9.8l2.5 2.2-1.4 2.2C7.4 14.3 1.7 8.6 1.8 2.9Z"/></svg>
        </li>
        <li>info@quorvane.com
          <svg viewBox="0 0 16 16" aria-hidden="true"><rect x="1" y="3" width="14" height="10" rx="1" fill="#e03a26"/><path d="M1.5 3.5 8 9l6.5-5.5" fill="none" stroke="#241a2b" stroke-width="1.3"/></svg>
        </li>
        <li>www.quorvane.com
          <svg viewBox="0 0 16 16" aria-hidden="true"><circle cx="8" cy="8" r="6.5" fill="none" stroke="#e03a26" stroke-width="1.5"/><path d="M1.5 8h13M8 1.5c-3 3.5-3 9.5 0 13M8 1.5c3 3.5 3 9.5 0 13" fill="none" stroke="#e03a26" stroke-width="1.2"/></svg>
        </li>
      </ul>
    </div>
  </section>

</main>
</body>
</html>
```